strength and conditioning business focused on helping people move more efficiently

I need a business card designed for a Philadelphia based company called Trk Vlt Motion (pronounced Track Volt). We offer fitness professional services with the idea of helping people feel better and move optimally. We do this by designing and walking through individualized programs as well as minor soft tissue work. Our perfect client would be athletes but we will be marketing to parents who have children that are active They remember their former athletic days and want to get as close as possible back to that feeling. Attached will be the official logo and logo formats. I would love for the design to communicate trustworthy and creative. I would also love for the design to be square with rounded edges.

Target Market(s)

Parents of athletic children
former athletes
athletes

Industry/Entity Type

Fitness

Contact Information for Business Card

Business: Trk Vlt Performance
Name: Coach Garrett Ellison
Position: Strength and Conditioning Coach / Certified Personal Trainer
Contact: coach.ell@trkvlt-example.com
Text: (555)204-7719

Font styles to use
Serif
Sans Serif

Colors
fbee38
fbee3e
0255a3
3176b5
ffffff

Requirements
Must have
• use of logo
Nice to have
• Square design
rounded edges

```html
<!DOCTYPE html>
<html lang="en">
<head>
<meta charset="utf-8">
<title>Trk Vlt Motion — Business Card</title>
<link rel="stylesheet" href="https://fonts.googleapis.com/css2?family=Montserrat:wght@400;700;800&display=swap">
<style>
  :root {
    --backdrop: #c3c2c3;
    --navy: #1d2f6b;
    --gold: #fdc70c;
    --white: #ffffff;
    --ink: #1f1f24;
  }
  * { margin: 0; padding: 0; box-sizing: border-box; }
  html, body { width: 1200px; height: 900px; overflow: hidden; }
  body {
    background: var(--backdrop);
    font-family: "Montserrat", Arial, sans-serif;
    position: relative;
  }
  .card {
    position: absolute;
    width: 424px;
    height: 422px;
    border-radius: 26px;
    overflow: hidden;
  }
  .card--front { left: 146px; top: 236px; background: var(--white); }
  .card--back { left: 634px; top: 232px; background: var(--navy); }

  .brand {
    position: absolute;
    display: flex;
    align-items: center;
    gap: 14px;
  }
  .brand__dot {
    flex: none;
    border-radius: 50%;
    border: 4px solid var(--gold);
  }
  .brand__name {
    font-weight: 800;
    letter-spacing: 0.5px;
    white-space: nowrap;
  }
  .card--front .brand { left: 28px; top: 76px; }
  .card--front .brand__dot { width: 48px; height: 48px; }
  .card--front .brand__name { color: var(--navy); font-size: 36px; }

  .card--back .brand {
    left: 0; right: 0; top: 150px;
    flex-direction: column;
    gap: 26px;
  }
  .card--back .brand__dot { width: 66px; height: 66px; }
  .card--back .brand__name { color: var(--white); font-size: 46px; }

  .person { position: absolute; left: 32px; top: 222px; }
  .person__name {
    color: var(--navy);
    font-weight: 700;
    font-size: 25px;
    line-height: 1.2;
  }
  .person__role {
    color: var(--ink);
    font-size: 16.5px;
    line-height: 19px;
    margin-top: 3px;
  }
  .person__rule {
    width: 32px; height: 2px;
    background: var(--navy);
    margin-top: 8px;
  }
  .contact {
    position: absolute;
    left: 34px; top: 316px;
    list-style: none;
  }
  .contact__item {
    display: flex;
    align-items: center;
    gap: 11px;
    height: 25px;
    color: var(--ink);
    font-size: 17px;
  }
  .contact__icon { width: 14px; height: 14px; flex: none; fill: var(--navy); }
</style>
</head>
<body>
  <section class="card card--front" aria-label="Business card front">
    <div class="brand">
      <span class="brand__dot"></span>
      <span class="brand__name">Trk Vlt Motion</span>
    </div>
    <div class="person">
      <h1 class="person__name">Coach Garrett Ellison</h1>
      <p class="person__role">Strength and Conditioning Coach<br>Certified Personal Trainer</p>
      <div class="person__rule"></div>
    </div>
    <ul class="contact">
      <li class="contact__item">
        <svg class="contact__icon" viewBox="0 0 16 16" aria-hidden="true"><path d="M1 6c0-2 3-4 7-4s7 2 7 4v1h-3V5.5H4V7H1z"/><path d="M3 8h10l1 6H2z"/></svg>
        (555)204-7719
      </li>
      <li class="contact__item">
        <svg class="contact__icon" viewBox="0 0 16 16" aria-hidden="true"><path d="M1 3h14v1.5L8 9 1 4.5z"/><path d="M1 6.3l7 4.5 7-4.5V13H1z"/></svg>
        coach.ell@trkvlt-example.com
      </li>
      <li class="contact__item">
        <svg class="contact__icon" viewBox="0 0 16 16" aria-hidden="true"><circle cx="8" cy="8" r="7"/><path d="M4 5q2 1 3 3t-1 4M10 3q1 3 3 4" stroke="#fff" stroke-width="1.3" fill="none"/></svg>
        www.trkvlt-example.com
      </li>
    </ul>
  </section>

  <section class="card card--back" aria-label="Business card back">
    <div class="brand">
      <span class="brand__dot"></span>
      <span class="brand__name">Trk Vlt Motion</span>
    </div>
  </section>
</body>
</html>
```